Summer Resolution Do it Now

I run a hypnotherapy practice that helps people
Loose Weight,Stop smoking ,overcome fear of Public speaking and improve Confidence and positive attitude.
I like to market a especific group in the CBD Melbourne as I only practice once a week in the city.

I have some photographs that will go well for the flyer what I am after is something very professional ,sober and elegant.

Target Market(s)

CBD corporate Melbourne market 25 till 60 year old

Industry/Entity Type

Hypnotherapy

Requirements
Must have
• flyer should be two sided , must have http://www.calmtranceclinic.example/ and the phone number 0427916058 and encourage to book online .

```html
<!DOCTYPE html>
<html lang="en">
<head>
<meta charset="utf-8">
<title>Daniel Harrow – Melbourne Hypnotherapist Flyer</title>
<link rel="stylesheet" href="https://fonts.googleapis.com/css2?family=Arimo:ital,wght@0,400;0,700;1,700&family=Roboto+Condensed:wght@400;700&family=Tinos&display=swap">
<style>
:root{
  --page:#3f4542;
  --front-tint:#dcecee;
  --ink:#222;
  --ink-soft:#333;
  --grey-phone:#5c5c5c;
  --brand-blue:#1b6fc2;
  --panel-blue:#0b74c5;
  --button-top:#3aa0ec;
  --button-bottom:#0a5fb4;
  --arrow-blue:#1b6fc2;
  --arrow-red:#e8502f;
  --bullet-red:#d8262c;
  --white:#fff;
  --rule:#9ab6cf;
}
*{margin:0;padding:0;box-sizing:border-box}
html,body{width:991px;height:1200px;overflow:hidden;background:var(--page)}
body{position:relative;font-family:"Arimo",Arial,sans-serif;color:var(--ink)}
.side-label{position:absolute;left:52px;font-family:"Tinos","Times New Roman",serif;font-size:38px;color:var(--white);line-height:1}
.side-label--front{top:8px}
.side-label--back{top:1150px}
.card{position:absolute;left:52px;width:886px;height:521px;overflow:hidden}
.card--front{top:52px;background:linear-gradient(100deg,#e6f2f2 0%,var(--front-tint) 55%,#cfe2e6 100%)}
.card--back{top:622px;background:var(--white)}
.abs{position:absolute}
.photo{position:absolute}
.front__photo{left:430px;top:0;width:456px;height:395px;
  background:radial-gradient(ellipse at 62% 40%,#f1d7c4 0%,#e9c9b0 20%,#d3bfa8 36%,#5aaa78 60%,#2e8a57 80%,#3f9465 100%);
  -webkit-mask-image:linear-gradient(90deg,transparent 0%,transparent 28%,#000 48%);
  mask-image:linear-gradient(90deg,transparent 0%,transparent 28%,#000 48%)}
.front__intro{left:44px;top:42px;font-size:25.5px;color:var(--ink);position:absolute}
.front__headline{left:43px;top:75px;font-size:43px;font-weight:400;color:var(--ink);letter-spacing:-.3px;position:absolute}
.front__text{left:45px;top:132px;width:515px;font-size:15px;line-height:20px;color:var(--ink-soft);position:absolute}
.treat__title{left:42px;top:267px;font-family:"Roboto Condensed",sans-serif;font-weight:700;font-size:20px;color:var(--brand-blue)}
.treat__list{list-style:none;font-family:"Roboto Condensed",sans-serif;font-size:16.5px;color:var(--ink)}
.treat__list li{height:24px;display:flex;align-items:center;gap:8px}
.treat__list--a{left:42px;top:300px}
.treat__list--b{left:232px;top:300px}
.arrow-icon{width:14px;height:14px;flex:none}
.front__base{left:0;top:385px;width:886px;height:136px}
.button{position:absolute;display:flex;align-items:center;justify-content:center;color:var(--white);font-size:28px;border-radius:8px;background:linear-gradient(var(--button-top),var(--button-bottom));box-shadow:0 0 0 2px #7cc3f5 inset}
.front__book{left:49px;top:414px;width:219px;height:40px}
.front__phone{left:46px;top:462px;font-size:38px;color:var(--grey-phone);letter-spacing:.5px}
.brand__mark{left:360px;top:412px;width:86px;height:86px;border-radius:50%;background:var(--brand-blue)}
.brand__name{left:469px;top:428px;font-size:21px;color:var(--ink)}
.brand__role{left:469px;top:454px;font-size:18px;color:var(--ink);letter-spacing:1.6px;border-bottom:1px solid #666;padding-bottom:2px}
.brand__web{left:471px;top:479px;font-size:11.5px;color:var(--brand-blue);letter-spacing:2.2px}
.brand__divider{left:760px;top:410px;width:1px;height:86px;background:#666}
.badge{left:781px;top:419px;width:77px;height:77px;border-radius:50%;background:#8cc63e;box-shadow:0 0 0 4px var(--white),0 0 0 5px #555}
.back__panel{left:0;top:0;width:886px;height:521px}
.back__photo{left:0;top:0;width:340px;height:378px;
  background:radial-gradient(ellipse at 38% 35%,#d9a78a 0%,#c58f72 22%,#efe6d6 46%,#e8dcc8 60%,#3f8fd1 82%,#1e7acb 100%);
  -webkit-mask-image:linear-gradient(90deg,#000 70%,transparent 100%);
  mask-image:linear-gradient(90deg,#000 70%,transparent 100%)}
.back__name{left:330px;top:52px;font-size:31px;font-weight:400;color:var(--white)}
.back__name b{font-weight:700}
.back__title{left:330px;top:93px;font-size:14px;font-weight:700;font-style:italic;color:var(--white)}
.back__bio{left:330px;top:133px;width:268px;font-size:15px;line-height:20.3px;color:var(--white)}
.back__rule{left:636px;top:54px;width:1px;height:309px;background:var(--rule)}
.quote__title{left:668px;top:56px;font-size:17px;font-weight:700;color:var(--white)}
.quote__text{left:668px;top:98px;width:176px;font-size:15px;line-height:20.3px;color:var(--white)}
.quote__author{left:692px;top:352px;font-size:15px;font-weight:700;font-style:italic;color:var(--white)}
.back__contact{left:634px;top:394px;width:218px;height:40px}
.prices{left:30px;top:398px;list-style:none;font-size:15px;color:var(--brand-blue)}
.prices li{height:26px;display:flex;align-items:center;gap:10px}
.prices b{font-weight:700}
.locations{left:518px;top:446px;list-style:none;font-size:14.5px;line-height:20px;color:var(--ink)}
.locations li{position:relative;padding-left:16px}
.locations li::before{content:"";position:absolute;left:0;top:6px;width:6px;height:6px;background:var(--bullet-red)}
.locations .note{color:var(--bullet-red)}
</style>
</head>
<body>

<div class="side-label side-label--front">Front</div>

<section class="card card--front">
  <div class="photo front__photo" role="img" aria-label="Photo of a smiling woman in a green top with glasses on her head"></div>

  <p class="front__intro">Daniel has treated everything from</p>
  <h1 class="front__headline">Fear of Flying to Hair Pulling</h1>
  <p class="front__text">Hypnotherapy is a powerful tool and can assist you in making desired changes to your life such as helping you quit smoking, lose weight or to improve public speaking among many other things.&nbsp; Daniel Harrow is a Clinical Hypnotherapist based in Melbourne’s CBD and Western Suburbs (Footscray). People from all over Australia come to see Daniel for hypnotherapy consultations.</p>

  <h2 class="abs treat__title">Hypnosis has been used to treat:</h2>
  <ul class="abs treat__list treat__list--a">
    <li><svg class="arrow-icon" viewBox="0 0 14 14"><circle cx="7" cy="7" r="6" fill="none" stroke="var(--arrow-blue)" stroke-width="2"/><path d="M4 7h6M7.5 4.5L10 7 7.5 9.5" fill="none" stroke="var(--arrow-blue)" stroke-width="2"/></svg>Stopping Smoking</li>
    <li><svg class="arrow-icon" viewBox="0 0 14 14"><circle cx="7" cy="7" r="6" fill="none" stroke="var(--arrow-blue)" stroke-width="2"/><path d="M4 7h6M7.5 4.5L10 7 7.5 9.5" fill="none" stroke="var(--arrow-blue)" stroke-width="2"/></svg>Alcohol Moderation</li>
    <li><svg class="arrow-icon" viewBox="0 0 14 14"><circle cx="7" cy="7" r="6" fill="none" stroke="var(--arrow-blue)" stroke-width="2"/><path d="M4 7h6M7.5 4.5L10 7 7.5 9.5" fill="none" stroke="var(--arrow-blue)" stroke-width="2"/></svg>Losing Weight</li>
    <li><svg class="arrow-icon" viewBox="0 0 14 14"><circle cx="7" cy="7" r="6" fill="none" stroke="var(--arrow-blue)" stroke-width="2"/><path d="M4 7h6M7.5 4.5L10 7 7.5 9.5" fill="none" stroke="var(--arrow-blue)" stroke-width="2"/></svg>Public Speaking Fears</li>
  </ul>
  <ul class="abs treat__list treat__list--b">
    <li><svg class="arrow-icon" viewBox="0 0 14 14"><circle cx="7" cy="7" r="6" fill="none" stroke="var(--arrow-blue)" stroke-width="2"/><path d="M4 7h6M7.5 4.5L10 7 7.5 9.5" fill="none" stroke="var(--arrow-blue)" stroke-width="2"/></svg>Bruxism / Teeth Grinding / Teeth</li>
    <li><svg class="arrow-icon" viewBox="0 0 14 14"><circle cx="7" cy="7" r="6" fill="none" stroke="var(--arrow-blue)" stroke-width="2"/><path d="M4 7h6M7.5 4.5L10 7 7.5 9.5" fill="none" stroke="var(--arrow-blue)" stroke-width="2"/></svg>Clenching</li>
    <li><svg class="arrow-icon" viewBox="0 0 14 14"><circle cx="7" cy="7" r="6" fill="none" stroke="var(--arrow-blue)" stroke-width="2"/><path d="M4 7h6M7.5 4.5L10 7 7.5 9.5" fill="none" stroke="var(--arrow-blue)" stroke-width="2"/></svg>IBS</li>
  </ul>

  <svg class="abs front__base" viewBox="0 0 886 136" preserveAspectRatio="none"><path d="M0 50 C 200 50 290 46 330 28 C 360 12 380 8 420 8 L886 8 L886 136 L0 136 Z" fill="var(--white)"/></svg>

  <div class="button front__book">BOOK NOW</div>
  <p class="abs front__phone">0427 916 058</p>

  <div class="abs brand__mark"></div>
  <p class="abs brand__name">Daniel Harrow</p>
  <p class="abs brand__role">Melbourne Hypnotherapist</p>
  <p class="abs brand__web">www.CalmTranceClinic.example</p>
  <div class="abs brand__divider"></div>
  <div class="abs badge"></div>
</section>

<section class="card card--back">
  <svg class="abs back__panel" viewBox="0 0 886 521" preserveAspectRatio="none"><path d="M0 0 H886 V432 H560 C 500 432 480 378 420 378 H0 Z" fill="var(--panel-blue)"/></svg>
  <div class="photo back__photo" role="img" aria-label="Portrait photo of the hypnotherapist in glasses and a cream shirt"></div>

  <h2 class="abs back__name"><b>Daniel</b> Harrow</h2>
  <p class="abs back__title">Qualified Clinical Hypnotherapist</p>
  <p class="abs back__bio">Daniel Harrow, qualified Clinical Hypnotherapist, focuses on helping each client to achieve their personal goals and improve their overall health and well being.&nbsp; In additional to clinical practice, Daniel is pursuing clinical research into the benefits of combining hypnotherapy with complementary treatment modalities to combat depression.</p>

  <div class="abs back__rule"></div>
  <h3 class="abs quote__title">Client Testimonial</h3>
  <p class="abs quote__text">I found the treatment to be relaxing, meditative and relative to my needs and personal goals. Daniel’s professional approach made for a comfortable environment. I felt totally relaxed. Thank you Daniel for a fantastic experience!</p>
  <p class="abs quote__author">—Laura Whitfield</p>

  <div class="button back__contact">CONTACT</div>

  <ul class="abs prices">
    <li><svg class="arrow-icon" viewBox="0 0 14 14"><circle cx="7" cy="7" r="6" fill="none" stroke="var(--arrow-red)" stroke-width="2"/><path d="M4 7h6M7.5 4.5L10 7 7.5 9.5" fill="none" stroke="var(--arrow-red)" stroke-width="2"/></svg><span>Standard Consultation: <b>$135</b></span></li>
    <li><svg class="arrow-icon" viewBox="0 0 14 14"><circle cx="7" cy="7" r="6" fill="none" stroke="var(--arrow-red)" stroke-width="2"/><path d="M4 7h6M7.5 4.5L10 7 7.5 9.5" fill="none" stroke="var(--arrow-red)" stroke-width="2"/></svg><span>Quit Smoking Hypnotherapy Consultation: <b>$195</b></span></li>
    <li><svg class="arrow-icon" viewBox="0 0 14 14"><circle cx="7" cy="7" r="6" fill="none" stroke="var(--arrow-red)" stroke-width="2"/><path d="M4 7h6M7.5 4.5L10 7 7.5 9.5" fill="none" stroke="var(--arrow-red)" stroke-width="2"/></svg><span>Three Consultation Weight Loss Package: <b>$450</b></span></li>
    <li><svg class="arrow-icon" viewBox="0 0 14 14"><circle cx="7" cy="7" r="6" fill="none" stroke="var(--arrow-red)" stroke-width="2"/><path d="M4 7h6M7.5 4.5L10 7 7.5 9.5" fill="none" stroke="var(--arrow-red)" stroke-width="2"/></svg><span>Appointment length: <b>50 mins – 1 hour</b></span></li>
  </ul>

  <ul class="abs locations">
    <li>Quiet Room Studio Level 9, 42 Harbour Lane,<br>Melbourne CBD <span class="note">(Wednesday Only)</span></li>
    <li>Westside Wellness 118 Kensal Road, Footscray</li>
  </ul>
</section>

<div class="side-label side-label--back">Back</div>

</body>
</html>
```